依頼詳細
各デザインサイズ:1100㎜×450㎜
背景色:白色
フォント、矢印:アートな雰囲気(動きがあるお洒落な雰囲気)
フォント色:黒
フォントサイズ:規格内で目いっぱいの大きさ

内容:添付データの通り
※ホテル名は1列ではなく複数列でも可
※矢印の向きは変えずに形のみ変更可
※車マークはデザインに合うように変更

データ種類:①②③
各データ内は、ベースができましたら基本的に矢印の向きだけ変える形となります。
※ご提案時には、上記3種類のデータ添付をお願いいたします。

ベース案として、データを添付いたします。
参考にご利用ください。

何卒ご提案ご協力の程よろしくお願いいたします。
記載項目
ホテル名、矢印、車マーク、30秒
希望イメージ
シンプル 複雑
単色 カラフル
暗い 明るい
日常 高級
遊び心 厳粛
未来的 伝統的
女性的 男性的
希望する色
無彩色系
納品ファイル
• 高解像度JPG (.jpg)
• イラストレーター形式 (.ai)
補足説明
■ 選んだ理由

フォントやサイズ感が良く、実際に電柱に照らし合わせた中でイメージがGoodでした。

■ 提案者全員のお礼・コメント

お忙しい中、複数のご提案を頂きありがとうございました。
今後も定期的に依頼を上げていく予定ですので、機会がございましたらご助力をお願いいたします。

```html
<!DOCTYPE html>
<html lang="ja">
<head>
<meta charset="utf-8">
<title>Grove Hotel – 案内看板</title>
<link href="https://fonts.googleapis.com/css2?family=Dela+Gothic+One&family=Mochiy+Pop+One&family=Roboto+Slab:wght@800&family=Noto+Sans+JP:wght@900&display=swap" rel="stylesheet">
<style>
  :root {
    --paper: #ffffff;
    --ink: #111111;
    --frame: #6a6a6a;
  }
  html, body {
    margin: 0;
    padding: 0;
    width: 710px;
    height: 1200px;
    overflow: hidden;
    background: var(--paper);
  }
  .sprite { position: absolute; width: 0; height: 0; }
  .board {
    display: grid;
    grid-template-columns: repeat(4, 142px);
    grid-template-rows: repeat(3, 348px);
    column-gap: 30px;
    row-gap: 36px;
    padding: 42px 26px;
  }
  .sign {
    position: relative;
    box-sizing: border-box;
    border: 1.5px solid var(--frame);
    background: var(--paper);
    color: var(--ink);
  }
  .sign-name {
    position: absolute;
    top: 20px;
    left: 0;
    right: 0;
    height: 180px;
    margin: 0;
    display: flex;
    justify-content: center;
  }
  .sign-name__text {
    writing-mode: vertical-rl;
    line-height: 1.05;
  }
  .sign-name__text span { display: block; }
  .sign-name__text span + span { padding-top: 14px; }
  .sign-name--katakana .sign-name__text {
    font-family: "Dela Gothic One", sans-serif;
    font-size: 40px;
    letter-spacing: 0.02em;
  }
  .sign-name--latin .sign-name__text {
    font-family: "Roboto Slab", serif;
    font-weight: 800;
    font-size: 37px;
    line-height: 1.15;
  }
  .sign-name--latin .sign-name__text span + span { padding-top: 0; }
  .sign-name--hiragana .sign-name__text {
    font-family: "Mochiy Pop One", sans-serif;
    font-size: 40px;
  }
  .sign-arrow {
    position: absolute;
    top: 212px;
    left: 41px;
    width: 60px;
    height: 60px;
  }
  .sign-foot {
    position: absolute;
    left: 0;
    right: 0;
    bottom: 18px;
    display: flex;
    align-items: center;
    justify-content: center;
    gap: 8px;
  }
  .sign-foot__car { width: 34px; height: 22px; }
  .sign-foot__time {
    font-family: "Noto Sans JP", sans-serif;
    font-weight: 900;
    font-size: 16px;
  }
</style>
</head>
<body>
<svg class="sprite" aria-hidden="true">
  <defs>
    <marker id="head" viewBox="0 0 10 10" refX="4" refY="5" markerWidth="3" markerHeight="3" orient="auto">
      <path d="M0 0 L10 5 L0 10 Z" fill="#111"/>
    </marker>
    <symbol id="arrow-up" viewBox="0 0 60 60">
      <path d="M30 58 V16" fill="none" stroke="#111" stroke-width="5" marker-end="url(#head)"/>
    </symbol>
    <symbol id="arrow-left" viewBox="0 0 60 60">
      <path d="M54 30 H16" fill="none" stroke="#111" stroke-width="5" marker-end="url(#head)"/>
    </symbol>
    <symbol id="arrow-right" viewBox="0 0 60 60">
      <path d="M6 30 H44" fill="none" stroke="#111" stroke-width="5" marker-end="url(#head)"/>
    </symbol>
    <symbol id="arrow-turn-right" viewBox="0 0 60 60">
      <path d="M20 58 V24 H42" fill="none" stroke="#111" stroke-width="5" marker-end="url(#head)"/>
    </symbol>
    <symbol id="arrow-bear-right" viewBox="0 0 60 60">
      <path d="M20 58 V24 L38 42" fill="none" stroke="#111" stroke-width="5" marker-end="url(#head)"/>
    </symbol>
    <symbol id="arrow-u-turn" viewBox="0 0 60 60">
      <path d="M20 58 V26 A12 12 0 0 1 44 26 V38" fill="none" stroke="#111" stroke-width="5" marker-end="url(#head)"/>
    </symbol>
    <symbol id="car" viewBox="0 0 34 22">
      <path d="M3 12 L7 4 Q8 2 10 2 H24 Q26 2 27 4 L31 12 Q33 12 33 14 V18 H1 V14 Q1 12 3 12 Z" fill="#111"/>
      <path d="M9 11 L11 5 H23 L25 11 Z" fill="#fff"/>
      <circle cx="8" cy="19" r="3" fill="#111"/>
      <circle cx="26" cy="19" r="3" fill="#111"/>
      <rect x="3" y="14" width="4" height="2" fill="#fff"/>
      <rect x="27" y="14" width="4" height="2" fill="#fff"/>
    </symbol>
  </defs>
</svg>

<main class="board">
  <!-- Katakana row -->
  <section class="sign">
    <h2 class="sign-name sign-name--katakana"><span class="sign-name__text"><span>グローブ</span><span>ホテル</span></span></h2>
    <svg class="sign-arrow" aria-label="直進"><use href="#arrow-up"/></svg>
    <div class="sign-foot"><svg class="sign-foot__car" aria-label="車"><use href="#car"/></svg><span class="sign-foot__time">30秒</span></div>
  </section>
  <section class="sign">
    <h2 class="sign-name sign-name--katakana"><span class="sign-name__text"><span>グローブ</span><span>ホテル</span></span></h2>
    <svg class="sign-arrow" aria-label="右折"><use href="#arrow-turn-right"/></svg>
    <div class="sign-foot"><svg class="sign-foot__car" aria-label="車"><use href="#car"/></svg><span class="sign-foot__time">30秒</span></div>
  </section>
  <section class="sign">
    <h2 class="sign-name sign-name--katakana"><span class="sign-name__text"><span>グローブ</span><span>ホテル</span></span></h2>
    <svg class="sign-arrow" aria-label="右斜め"><use href="#arrow-bear-right"/></svg>
    <div class="sign-foot"><svg class="sign-foot__car" aria-label="車"><use href="#car"/></svg><span class="sign-foot__time">30秒</span></div>
  </section>
  <section class="sign">
    <h2 class="sign-name sign-name--katakana"><span class="sign-name__text"><span>グローブ</span><span>ホテル</span></span></h2>
    <svg class="sign-arrow" aria-label="Uターン"><use href="#arrow-u-turn"/></svg>
    <div class="sign-foot"><svg class="sign-foot__car" aria-label="車"><use href="#car"/></svg><span class="sign-foot__time">30秒</span></div>
  </section>

  <!-- Latin row -->
  <section class="sign">
    <h2 class="sign-name sign-name--latin"><span class="sign-name__text"><span>Grove</span><span>Hotel</span></span></h2>
    <svg class="sign-arrow" aria-label="左"><use href="#arrow-left"/></svg>
    <div class="sign-foot"><svg class="sign-foot__car" aria-label="車"><use href="#car"/></svg><span class="sign-foot__time">30秒</span></div>
  </section>
  <section class="sign">
    <h2 class="sign-name sign-name--latin"><span class="sign-name__text"><span>Grove</span><span>Hotel</span></span></h2>
    <svg class="sign-arrow" aria-label="右"><use href="#arrow-right"/></svg>
    <div class="sign-foot"><svg class="sign-foot__car" aria-label="車"><use href="#car"/></svg><span class="sign-foot__time">30秒</span></div>
  </section>
  <section class="sign">
    <h2 class="sign-name sign-name--latin"><span class="sign-name__text"><span>Grove</span><span>Hotel</span></span></h2>
    <svg class="sign-arrow" aria-label="直進"><use href="#arrow-up"/></svg>
    <div class="sign-foot"><svg class="sign-foot__car" aria-label="車"><use href="#car"/></svg><span class="sign-foot__time">30秒</span></div>
  </section>
  <section class="sign">
    <h2 class="sign-name sign-name--latin"><span class="sign-name__text"><span>Grove</span><span>Hotel</span></span></h2>
    <svg class="sign-arrow" aria-label="Uターン"><use href="#arrow-u-turn"/></svg>
    <div class="sign-foot"><svg class="sign-foot__car" aria-label="車"><use href="#car"/></svg><span class="sign-foot__time">30秒</span></div>
  </section>

  <!-- Hiragana row -->
  <section class="sign">
    <h2 class="sign-name sign-name--hiragana"><span class="sign-name__text"><span>ぐろーぶ</span><span>ほてる</span></span></h2>
    <svg class="sign-arrow" aria-label="直進"><use href="#arrow-up"/></svg>
    <div class="sign-foot"><svg class="sign-foot__car" aria-label="車"><use href="#car"/></svg><span class="sign-foot__time">30秒</span></div>
  </section>
  <section class="sign">
    <h2 class="sign-name sign-name--hiragana"><span class="sign-name__text"><span>ぐろーぶ</span><span>ほてる</span></span></h2>
    <svg class="sign-arrow" aria-label="右折"><use href="#arrow-turn-right"/></svg>
    <div class="sign-foot"><svg class="sign-foot__car" aria-label="車"><use href="#car"/></svg><span class="sign-foot__time">30秒</span></div>
  </section>
  <section class="sign">
    <h2 class="sign-name sign-name--hiragana"><span class="sign-name__text"><span>ぐろーぶ</span><span>ほてる</span></span></h2>
    <svg class="sign-arrow" aria-label="右斜め"><use href="#arrow-bear-right"/></svg>
    <div class="sign-foot"><svg class="sign-foot__car" aria-label="車"><use href="#car"/></svg><span class="sign-foot__time">30秒</span></div>
  </section>
  <section class="sign">
    <h2 class="sign-name sign-name--hiragana"><span class="sign-name__text"><span>ぐろーぶ</span><span>ほてる</span></span></h2>
    <svg class="sign-arrow" aria-label="Uターン"><use href="#arrow-u-turn"/></svg>
    <div class="sign-foot"><svg class="sign-foot__car" aria-label="車"><use href="#car"/></svg><span class="sign-foot__time">30秒</span></div>
  </section>
</main>
</body>
</html>
```